Mesa Bloom

We have opened new business that includes pottery & chimineas we want cards to have collage of pictures of products on front of card then information on back. On back in middle MESA BLOOM +
marlo_tesh@fernmail.example
(555) 318-2274
(555)3182917 & mesabloom@fernmail.example
Business
Sans Serif
Decorative

```html
<!DOCTYPE html>
<html lang="en">
<head>
<meta charset="utf-8">
<title>Mesa Bloom — Business Card Back</title>
<link rel="stylesheet" href="https://fonts.googleapis.com/css2?family=Cinzel:wght@700&family=Josefin+Sans:wght@100;300&display=swap">
<style>
  :root {
    --card-sage: #bfbf98;
    --ink-white: #ffffff;
    --ink-soft: #ecece0;
  }
  html, body {
    margin: 0;
    padding: 0;
    width: 1200px;
    height: 796px;
    overflow: hidden;
    background: var(--card-sage);
  }
  .card-back {
    position: relative;
    width: 1200px;
    height: 796px;
    background: var(--card-sage);
  }
  .card-line {
    position: absolute;
    left: 0;
    width: 100%;
    margin: 0;
    text-align: center;
    line-height: 1;
    white-space: nowrap;
  }
  .business-name {
    top: 90px;
    font-family: "Cinzel", "Times New Roman", serif;
    font-weight: 700;
    font-size: 74px;
    letter-spacing: 5px;
    color: var(--ink-white);
  }
  .owner-names {
    top: 208px;
    font-family: "Josefin Sans", "Helvetica", sans-serif;
    font-weight: 300;
    font-size: 100px;
    letter-spacing: 2px;
    color: var(--ink-white);
  }
  .contact {
    font-family: "Josefin Sans", "Helvetica", sans-serif;
    font-weight: 100;
    color: var(--ink-soft);
  }
  .contact-phones {
    top: 372px;
    font-size: 52px;
  }
  .contact-email {
    font-size: 46px;
  }
  .contact-email--personal { top: 454px; }
  .contact-email--shop { top: 537px; }
</style>
</head>
<body>
  <main class="card-back">
    <h1 class="card-line business-name">Mesa Bloom +</h1>
    <p class="card-line owner-names">Marlo &amp; Nadia Tesh</p>
    <p class="card-line contact contact-phones">(555) 318-2274 | (555) 318-2917</p>
    <p class="card-line contact contact-email contact-email--personal">Marlo_tesh@fernmail.example</p>
    <p class="card-line contact contact-email contact-email--shop">mesabloom@fernmail.example</p>
  </main>
</body>
</html>
```